Pebble and Pine App design

I need a full app design, colours, images, fonts, and a mock up design of the app to bring to the developer.

Pebble and Pine is a free app that allows cafes, independent cafe and chains of cafes to let their customers know what the soup of the day and what specials they have on that day through the app. Each cafe will have a profile which they can upload the Pebble and Pine daily.

The user home screen will include google maps showing their location with the registered cafes and eateries around them. including a list of the cafe and distances below. as seen in attachment.

Target Market(s)

Cafes , anyone who enjoys eating soups and off local cafe specials boards

Requirements
Must have
• I would like a complete app design based on the attached images.

```html
<!DOCTYPE html>
<html lang="en">
<head>
<meta charset="utf-8">
<title>Pebble and Pine – App Screens</title>
<link rel="stylesheet" href="https://fonts.googleapis.com/css2?family=Roboto:wght@700&family=Nunito+Sans:wght@400;600;700;800&display=swap">
<style>
  :root {
    --brand: #e75857;
    --white: #ffffff;
    --ink-soft: #6b6b6b;
    --screen-edge: rgba(255,255,255,0.35);
    --map-light: #eeeeec;
    --map-mid: #e2e4df;
    --map-park: #cfe8c4;
    --pin-tail: #6f8fa6;
  }
  * { margin: 0; padding: 0; box-sizing: border-box; }
  html, body { width: 1200px; height: 1200px; overflow: hidden; }
  body {
    background: var(--brand);
    color: var(--white);
    font-family: "Nunito Sans", sans-serif;
    position: relative;
  }
  .board-title {
    position: absolute; top: 150px; left: 0; width: 100%;
    text-align: center;
    font-family: "Roboto", sans-serif; font-weight: 700;
    font-size: 76px; letter-spacing: 0.5px;
  }
  .screen-label {
    position: absolute; top: 300px; width: 380px;
    text-align: center; font-size: 36px; font-weight: 400;
    letter-spacing: 0.5px;
  }
  .screen {
    position: absolute; top: 400px; width: 251px; height: 543px;
    border-radius: 30px; border: 2px solid var(--screen-edge);
    background: var(--brand); overflow: hidden;
  }
  .status-bar {
    position: absolute; top: 4px; left: 0; width: 100%; height: 16px;
    display: flex; justify-content: space-between; align-items: center;
    padding: 0 12px 0 16px; font-size: 10px; font-weight: 700;
    font-family: "Roboto", sans-serif;
  }
  .status-icons { display: flex; gap: 4px; align-items: center; }
  .brand-mark {
    position: absolute; left: 50%; transform: translateX(-50%);
    width: 34px; height: 34px; border-radius: 50%; background: var(--white);
  }
  .brand-name {
    position: absolute; left: 0; width: 100%; text-align: center;
    font-weight: 800; font-size: 16px;
  }
  .tagline {
    position: absolute; left: 0; width: 100%; text-align: center;
    font-size: 13px;
  }
  /* Homepage */
  .role-card {
    position: absolute; top: 293px; width: 96px; height: 98px;
    background: var(--white); border-radius: 12px; color: var(--brand);
    text-align: center;
  }
  .role-card svg { position: absolute; top: 20px; left: 50%; transform: translateX(-50%); }
  .role-card .role-name {
    position: absolute; bottom: 8px; left: 0; width: 100%;
    font-weight: 800; font-size: 12px;
  }
  /* Registration */
  .field {
    position: absolute; left: 21px; width: 208px; height: 34px;
    background: var(--white); border-radius: 17px;
    color: var(--ink-soft); font-size: 9px; padding-left: 15px;
    display: flex; align-items: center;
  }
  .terms {
    position: absolute; top: 381px; left: 0; width: 100%;
    text-align: center; font-size: 8.5px; line-height: 13px; opacity: 0.95;
  }
  .register-btn {
    position: absolute; top: 419px; left: 65px; width: 119px; height: 34px;
    background: var(--white); border-radius: 17px; color: var(--brand);
    display: flex; align-items: center; justify-content: center; gap: 10px;
    font-weight: 800; font-size: 12px;
  }
  /* Logged-in home */
  .map-area {
    position: absolute; top: 40px; left: 0; width: 100%; height: 470px;
    background: linear-gradient(160deg, var(--map-light) 0%, var(--map-mid) 55%, var(--map-park) 70%, var(--map-light) 85%);
  }
  .app-header {
    position: absolute; top: 0; left: 0; width: 100%; height: 70px;
    background: var(--brand); border-radius: 0 0 28px 28px;
  }
  .app-header .brand-name { top: 36px; }
  .search-bar {
    position: absolute; top: 81px; left: 17px; width: 218px; height: 31px;
    background: var(--white); border-radius: 16px;
    display: flex; align-items: center; gap: 10px; padding: 0 12px 0 16px;
    color: var(--ink-soft); font-size: 8.5px;
    box-shadow: 0 2px 6px rgba(0,0,0,0.12);
  }
  .search-bar .filter { margin-left: auto; }
  .price-tag {
    position: absolute; height: 22px; border-radius: 11px;
    background: var(--brand); border: 1.5px solid var(--white);
    font-size: 7px; font-weight: 800; display: flex; align-items: center;
    justify-content: center; white-space: nowrap;
    box-shadow: 0 2px 4px rgba(0,0,0,0.15);
  }
  .price-tag::after {
    content: ""; position: absolute; left: 50%; bottom: -7px; transform: translateX(-50%);
    border-left: 5px solid transparent; border-right: 5px solid transparent;
    border-top: 7px solid var(--pin-tail);
  }
  .tab-bar {
    position: absolute; bottom: 0; left: 0; width: 100%; height: 44px;
    background: var(--brand); border-radius: 26px 26px 0 0;
    display: flex; justify-content: space-around; align-items: center;
    padding-top: 2px;
  }
</style>
</head>
<body>

  <h1 class="board-title">Pebble and Pine</h1>

  <div class="screen-label" style="left:27px;">Homepage</div>
  <div class="screen-label" style="left:402px;">Registration</div>
  <div class="screen-label" style="left:778px;">Homepage With Login</div>

  <!-- Homepage -->
  <section class="screen" style="left:91px;">
    <div class="brand-mark" style="top:150px;"></div>
    <div class="brand-name" style="top:214px;">Pebble and Pine</div>
    <p class="tagline" style="top:258px;">Want to Taste Or Serve ?</p>

    <div class="role-card" style="left:22px;">
      <svg width="40" height="42" viewBox="0 0 40 42" fill="none" stroke="currentColor" stroke-width="3" stroke-linecap="round">
        <path d="M6 2v12M11 2v12M16 2v12M6 14h10M11 14v26"/>
        <path d="M22 2c4 4 4 14 0 16v22"/>
        <ellipse cx="33" cy="9" rx="4" ry="7" fill="currentColor"/>
        <path d="M33 16v24"/>
      </svg>
      <span class="role-name">Taste</span>
    </div>

    <div class="role-card" style="left:132px;">
      <svg width="50" height="44" viewBox="0 0 50 44" fill="none" stroke="currentColor" stroke-width="2.6" stroke-linecap="round">
        <path d="M6 16 Q25 -2 44 16Z" fill="currentColor"/>
        <path d="M25 4V34M14 26h22M4 22v18M4 32h9v8M46 22v18M46 32h-9v8M18 26v14M32 26v14"/>
      </svg>
      <span class="role-name">Serve</span>
    </div>
  </section>

  <!-- Registration -->
  <section class="screen" style="left:467px;">
    <div class="status-bar">
      <span>9:41</span>
      <span class="status-icons">
        <svg width="12" height="8" viewBox="0 0 12 8" fill="#fff"><rect x="0" y="5" width="2" height="3"/><rect x="3" y="3.5" width="2" height="4.5"/><rect x="6" y="2" width="2" height="6"/><rect x="9" y="0" width="2" height="8"/></svg>
        <svg width="11" height="8" viewBox="0 0 11 8" fill="none" stroke="#fff" stroke-width="1.4"><path d="M1 3a6.5 6.5 0 0 1 9 0M2.8 5a4 4 0 0 1 5.4 0"/><circle cx="5.5" cy="7" r="0.8" fill="#fff"/></svg>
        <svg width="16" height="8" viewBox="0 0 16 8"><rect x="0.5" y="0.5" width="13" height="7" rx="1.5" fill="#fff"/><rect x="14" y="2.5" width="1.5" height="3" fill="#fff"/></svg>
      </span>
    </div>
    <div class="brand-mark" style="top:110px;"></div>
    <div class="brand-name" style="top:164px;">Pebble and Pine</div>
    <p class="tagline" style="top:200px;">Register as a User</p>

    <div class="field" style="top:237px;">Email</div>
    <div class="field" style="top:283px;">Password</div>
    <div class="field" style="top:330px;">Enter Password Again</div>

    <p class="terms">Lorem Ipsum is dummy terms and conditions<br>he printing and typesetting industry.</p>

    <div class="register-btn">
      <svg width="18" height="18" viewBox="0 0 40 42" fill="none" stroke="currentColor" stroke-width="4" stroke-linecap="round">
        <path d="M6 2v12M11 2v12M16 2v12M6 14h10M11 14v26"/>
        <path d="M22 2c4 4 4 14 0 16v22"/>
        <ellipse cx="33" cy="9" rx="4" ry="7" fill="currentColor"/>
        <path d="M33 16v24"/>
      </svg>
      Register
    </div>
  </section>

  <!-- Homepage with login -->
  <section class="screen" style="left:843px;">
    <div class="map-area" role="img" aria-label="Street map of the city centre showing nearby cafes and points of interest"></div>

    <header class="app-header">
      <div class="status-bar">
        <span>9:41</span>
        <span class="status-icons">
          <svg width="12" height="8" viewBox="0 0 12 8" fill="#fff"><rect x="0" y="5" width="2" height="3"/><rect x="3" y="3.5" width="2" height="4.5"/><rect x="6" y="2" width="2" height="6"/><rect x="9" y="0" width="2" height="8"/></svg>
          <svg width="11" height="8" viewBox="0 0 11 8" fill="none" stroke="#fff" stroke-width="1.4"><path d="M1 3a6.5 6.5 0 0 1 9 0M2.8 5a4 4 0 0 1 5.4 0"/><circle cx="5.5" cy="7" r="0.8" fill="#fff"/></svg>
          <svg width="16" height="8" viewBox="0 0 16 8"><rect x="0.5" y="0.5" width="13" height="7" rx="1.5" fill="#fff"/><rect x="14" y="2.5" width="1.5" height="3" fill="#fff"/></svg>
        </span>
      </div>
      <div class="brand-name">Pebble and Pine</div>
    </header>

    <div class="search-bar">
      <svg width="11" height="11" viewBox="0 0 12 12" fill="none" stroke="#e75857" stroke-width="1.5"><circle cx="5" cy="5" r="4"/><path d="M8 8l3 3"/></svg>
      <span>Seach Soups</span>
      <svg class="filter" width="12" height="11" viewBox="0 0 12 11" fill="none" stroke="#e75857" stroke-width="1"><rect x="0.5" y="0.5" width="11" height="10" rx="2"/><path d="M3 3.5h6M3 5.5h6M3 7.5h6"/></svg>
    </div>

    <div class="price-tag" style="top:232px; left:131px; width:111px;">$500 - Murshroom Special</div>
    <div class="price-tag" style="top:320px; left:68px; width:96px;">$300 - Tomato Special</div>

    <nav class="tab-bar">
      <!-- home -->
      <svg width="15" height="14" viewBox="0 0 15 14" fill="#fff"><path d="M7.5 0.5L0.5 6.5h2v7h4v-4h2v4h4v-7h2z"/></svg>
      <!-- location pin -->
      <svg width="12" height="15" viewBox="0 0 12 15" fill="#fff"><path d="M6 0a6 6 0 0 1 6 6c0 4-6 9-6 9S0 10 0 6a6 6 0 0 1 6-6z"/><circle cx="6" cy="6" r="2.2" fill="#e75857"/></svg>
      <!-- profile -->
      <svg width="13" height="15" viewBox="0 0 13 15" fill="#fff"><circle cx="6.5" cy="4" r="3.5"/><path d="M0 15a6.5 6 0 0 1 13 0z"/></svg>
      <!-- settings -->
      <svg width="15" height="15" viewBox="0 0 16 16" fill="none" stroke="#fff" stroke-width="2"><circle cx="8" cy="8" r="2.5"/><circle cx="8" cy="8" r="5.5" stroke-dasharray="2.5 1.8"/></svg>
    </nav>
  </section>

</body>
</html>
```